Very Simple/Minimal Business Card Design Project

The company operates in the industrial maritime infrastructure sector in Brazil. You can find more information on our website www.navelquor.com.br WE NEED TO LOOK POWERFUL AND SERIOUS
I have attached a copy of the old cards. We would like something more professional / industrial / sexy that also includes the position.

The card can be double sided or not. We would like you to propose as many options.

Thank you
Updates

Many thanks, do let me know if you have any questions. I am under a lot of time pressure to try and have them printed over the next days or so.

Please could you use the following information

for the address: Rua Tapiraçu, 418 - Centro, Rio de Janeiro, 20135-070, Brasil

for the mobile: +55 21 8372 9041
for the landline: +55 21 4067 3859

and position:  Diretor Geral

Thakn you

Target Market(s)

Shipowners, bankers, industrial companies

Industry/Entity Type

Industrial

Requirements
Must have
• POWERFUL
SERIOUS
SOLID
BIG CORPORATION

```html
<!DOCTYPE html>
<html lang="pt-BR">
<head>
<meta charset="utf-8">
<title>Navelquor – Business Card</title>
<link rel="stylesheet" href="https://fonts.googleapis.com/css2?family=Source+Sans+3:wght@400;700;800&display=swap">
<style>
  :root {
    --navy: #1b2a78;
    --green: #2f9a36;
    --paper-light: #ffffff;
    --paper-grey: #d9dbdc;
    --ink: #111111;
    --white: #ffffff;
  }
  * { margin: 0; padding: 0; box-sizing: border-box; }
  html, body {
    width: 1200px; height: 796px; overflow: hidden;
    background: var(--white);
  }
  .card {
    position: relative;
    width: 1200px; height: 796px;
    overflow: hidden;
    font-family: "Source Sans 3", "Myriad Pro", Arial, sans-serif;
    color: var(--ink);
    background: linear-gradient(115deg, var(--paper-grey) 0%, #eceded 35%, var(--paper-light) 70%);
  }
  .card__shapes { position: absolute; inset: 0; width: 100%; height: 100%; }

  .brand {
    position: absolute; left: 100px; top: 54px;
    display: flex; align-items: center; gap: 22px;
  }
  .brand__square {
    width: 148px; height: 150px;
    background: var(--green);
  }
  .brand__name {
    font-weight: 800;
    font-size: 110px;
    line-height: 1;
    color: var(--navy);
    letter-spacing: 1px;
  }

  .person { position: absolute; left: 96px; top: 220px; }
  .person__name { font-size: 56px; font-weight: 400; line-height: 1.05; }
  .person__role { font-size: 40px; font-weight: 400; line-height: 1.3; }

  .address {
    position: absolute; left: 98px; top: 536px;
    font-size: 29px; line-height: 42px; font-style: normal;
  }
  .contacts {
    position: absolute; left: 680px; top: 536px;
    font-size: 29px; line-height: 42px;
    color: var(--white); list-style: none;
  }
</style>
</head>
<body>
  <div class="card">
    <svg class="card__shapes" viewBox="0 0 1200 796" preserveAspectRatio="none" aria-hidden="true">
      <defs>
        <linearGradient id="greenGlow" x1="1" y1="0" x2="0" y2="0">
          <stop offset="0" stop-color="#5cb446" stop-opacity="0.7"/>
          <stop offset="1" stop-color="#5cb446" stop-opacity="0"/>
        </linearGradient>
      </defs>
      <polygon points="975,0 430,796 270,796 885,0" fill="url(#greenGlow)" opacity="0.45"/>
      <polygon points="975,0 1025,0 480,796 430,796" fill="var(--green)"/>
      <polygon points="1025,0 1200,0 1200,796 480,796" fill="var(--navy)"/>
    </svg>

    <div class="brand">
      <span class="brand__square"></span>
      <span class="brand__name">NAVELQUOR</span>
    </div>

    <div class="person">
      <p class="person__name">Rafael Montenegro</p>
      <p class="person__role">Diretor Geral</p>
    </div>

    <address class="address">
      Address: Rua Tapiraçu, 418<br>
      - Centro, Rio de Janeiro,<br>
      20135-070,<br>
      Brasil
    </address>

    <ul class="contacts">
      <li>landline: +55 21 4067 3859</li>
      <li>Mobile: +55 21 8372 9041</li>
      <li>E-mail: rafael@navelquor.com.br</li>
      <li>www.navelquor.com.br</li>
    </ul>
  </div>
</body>
</html>
```